Stationery Design Project

KT7 Staffing requires letterhead and business card designs for a company based in London. Just like the name, we're a management resourcing company, providing resources to third party companies. You can see www.kt7staffing-example.com for ideas on existing colour schemes and design concepts that have been implimented and agreed to. Ultimately the design should broadcast professionalism, safety and the concept of growth.

Target Market(s)

Financial institutes; friendly societies (All UK based)

Industry/Entity Type

Safety

Requirements
Must have
• Files produced should be print ready; and the text in them editable (eg address, name etc)

```html
<!DOCTYPE html>
<html lang="en">
<head>
<meta charset="utf-8">
<title>KT7 Staffing – Stationery</title>
<link href="https://fonts.googleapis.com/css2?family=Source+Sans+3:wght@400;600&display=swap" rel="stylesheet">
<style>
  :root {
    --backdrop: #d9d9d9;
    --board: #ffffff;
    --sheet: #f6f6f8;
    --teal: #2a97a3;
    --teal-light: #4fb4c8;
    --ink: #333a44;
    --rule: #c9ccd2;
    --navy: #1f2b47;
  }
  * { box-sizing: border-box; margin: 0; padding: 0; }
  html, body { width: 1168px; height: 1200px; overflow: hidden; }
  body {
    background: var(--backdrop);
    font-family: "Source Sans 3", "Myriad Pro", Arial, sans-serif;
    color: var(--ink);
    position: relative;
  }
  .board {
    position: absolute; left: 25px; top: 25px;
    width: 1119px; height: 1148px;
    background: var(--board); border-radius: 44px;
  }
  /* Letterhead */
  .letterhead {
    position: absolute; left: 215px; top: 140px;
    width: 688px; height: 932px;
    background: var(--sheet);
  }
  .letterhead__brand {
    position: absolute; left: 54px; top: 42px;
    font-size: 38px; font-weight: 400; letter-spacing: 0.5px;
    color: var(--teal); line-height: 1;
  }
  .letterhead__address {
    position: absolute; left: 483px; top: 32px;
    font-size: 11px; line-height: 1.35; color: var(--ink);
  }
  .letterhead__address .company { font-size: 15px; color: var(--teal); margin-bottom: 3px; }
  .letterhead__rule {
    position: absolute; left: 0; top: 108px; width: 100%; height: 1px;
    background: var(--rule);
  }
  .letterhead__rule-accent {
    position: absolute; right: 0; top: 106px; width: 374px; height: 3px;
    background: var(--teal);
  }
  .letterhead__footer {
    position: absolute; left: 90px; top: 896px;
    font-size: 12px; white-space: nowrap;
  }
  .letterhead__footer .company { color: var(--teal); margin-right: 6px; }
  .letterhead__footer .label { color: var(--teal); margin: 0 6px 0 16px; }

  /* Cards */
  .card {
    position: absolute; width: 355px; height: 220px;
    border-radius: 12px;
    box-shadow: 5px 6px 6px rgba(0,0,0,0.22);
    overflow: hidden;
  }
  .card--front { left: 653px; top: 404px; background: #ffffff; border: 1px solid #e1e3e6; }
  .card--back { left: 651px; top: 636px; background: var(--navy); }
  .card__brand {
    position: absolute; left: 54px; top: 24px;
    font-size: 22px; color: var(--teal-light); line-height: 1;
  }
  .card--back .card__brand {
    left: 0; width: 100%; top: 96px; text-align: center; font-size: 24px;
  }
  .card__person { position: absolute; left: 20px; top: 118px; text-align: right; width: 122px; }
  .card__person .name { font-size: 15px; color: var(--teal); }
  .card__person .role { font-size: 10px; margin-top: 6px; }
  .card__details { position: absolute; left: 178px; top: 80px; font-size: 9.5px; line-height: 1.35; }
  .card__details .company { font-size: 14px; color: var(--teal); margin-bottom: 3px; }
  .card__contacts { list-style: none; margin-top: 12px; }
  .card__contacts li { line-height: 1.45; }
  .card__contacts .label { color: var(--teal); display: inline-block; width: 22px; }
</style>
</head>
<body>
  <div class="board">
  </div>

  <section class="letterhead">
    <div class="letterhead__brand">KT7 STAFFING</div>
    <address class="letterhead__address" style="font-style:normal">
      <div class="company">KT7 Staffing</div>
      24 Marlow Court<br>
      118 Fenwick Street - London<br>
      LX9 4QT - United Kingdom
    </address>
    <div class="letterhead__rule"></div>
    <div class="letterhead__rule-accent"></div>
    <div class="letterhead__footer">
      <span class="company">KT7 Staffing</span>www.kt7staffing-example.com
      <span class="label">T :</span>+44(0)20 7946 0018
      <span class="label">M :</span>+44(0)7700 900 412
    </div>
  </section>

  <section class="card card--front">
    <div class="card__brand">KT7 STAFFING</div>
    <div class="card__person">
      <div class="name">Daniel Hartley</div>
      <div class="role">Director</div>
    </div>
    <div class="card__details">
      <div class="company">KT7 Staffing</div>
      24 Marlow Court<br>
      118 Fenwick Street - London<br>
      LX9 4QT - United Kingdom
      <ul class="card__contacts">
        <li><span class="label">W :</span>www.kt7staffing-example.com</li>
        <li><span class="label">E :</span>daniel@kt7staffing-example.com</li>
        <li><span class="label">T :</span>+44(0)20 7946 0018</li>
        <li><span class="label">M :</span>+44(0)7700 900 412</li>
      </ul>
    </div>
  </section>

  <section class="card card--back">
    <div class="card__brand">KT7 STAFFING</div>
  </section>
</body>
</html>
```